I want a design for my parents 50th wedding anniversary , "road to 50 years" including key dates that are of importance to them. My parents are both classical musicians (mother = violin, father = French horn) so I was thinking that the road could be in the form of music sheets. My parents live in Germany and so the document attached with key dates is in German. I was thinking that whenever an event relates to my mother, Lore, a violin symbol should be used. When it relates to my father Berti a Frenchhorn symbol should be used. I am also proposing to use a graduate cap to indicate when my sister and I graduated (Abitur and Studienabschluss) and intertwined wedding rings for weddings (Hochzeit), a baby rattle for births (Geburt) and 2 toasting champagne glasses for Berti & Lore 50th anniversary (50. Hochzeitstag). For the other dates, if you can think of a good symbol please include.

```html
<!DOCTYPE html>
<html lang="de">
<head>
<meta charset="utf-8">
<title>Road to 50 Years</title>
<link rel="stylesheet" href="https://fonts.googleapis.com/css2?family=Oswald:wght@400;600&family=Yellowtail&display=swap">
<style>
  :root{
    --page:#fbf8ef;
    --frame:#2a1518;
    --ink:#2a1518;
    --paper-light:#fff8d6;
    --paper-mid:#fbe79a;
    --paper-warm:#f7c94a;
    --band-dark:#a8741f;
    --band-light:#f2cf74;
    --halo:#fff3c4;
  }
  html,body{margin:0;padding:0;overflow:hidden;background:var(--page);}
  .canvas{width:1200px;height:1200px;position:relative;overflow:hidden;background:var(--page);}
  .poster{position:absolute;inset:0;width:1200px;height:1200px;display:block;}
  .year{font-family:"Oswald",sans-serif;font-weight:600;font-size:25px;fill:var(--ink);text-anchor:middle;}
  .event{font-family:"Oswald",sans-serif;font-weight:400;font-size:25px;fill:var(--ink);text-anchor:middle;}
  .title{font-family:"Yellowtail",cursive;font-size:96px;fill:var(--ink);text-anchor:middle;}
  .clef{fill:none;stroke:var(--ink);stroke-width:9;stroke-linecap:round;stroke-linejoin:round;}
  .clef-dot{fill:var(--ink);}
  .staff-line{stroke:var(--ink);stroke-width:4;}
  .bar-line{stroke:var(--ink);stroke-width:5;}
  .final-bar{stroke:var(--ink);stroke-width:12;}
  .icon{color:var(--ink);}
</style>
</head>
<body>
<div class="canvas">
<svg class="poster" viewBox="0 0 1920 1920" xmlns="http://www.w3.org/2000/svg">
  <defs>
    <radialGradient id="paperGlow" cx="0.7" cy="0.85" r="0.9">
      <stop offset="0" stop-color="var(--paper-warm)"/>
      <stop offset="0.45" stop-color="var(--paper-mid)"/>
      <stop offset="1" stop-color="var(--paper-light)"/>
    </radialGradient>
    <linearGradient id="titleBand" x1="0" x2="1">
      <stop offset="0" stop-color="var(--band-dark)"/>
      <stop offset="0.5" stop-color="var(--band-light)"/>
      <stop offset="1" stop-color="var(--band-dark)"/>
    </linearGradient>

    <symbol id="violin" viewBox="-50 -50 100 100">
      <g transform="rotate(28)" fill="currentColor">
        <rect x="-3.5" y="-50" width="7" height="52" rx="2"/>
        <circle cx="0" cy="-48" r="5"/>
        <ellipse cx="0" cy="-6" rx="14" ry="13"/>
        <ellipse cx="0" cy="20" rx="19" ry="17"/>
        <rect x="-9" y="4" width="18" height="6"/>
        <path d="M-6 2 v18 M6 2 v18" stroke="var(--halo)" stroke-width="2"/>
        <path d="M-1.5 -30 V32 M1.5 -30 V32" stroke="var(--halo)" stroke-width="1"/>
      </g>
    </symbol>

    <symbol id="horn" viewBox="-50 -50 100 100">
      <g fill="currentColor">
        <path d="M-22 -46 L-6 -38 C-12 -26 -8 -10 8 -4 L0 6 C-16 -2 -26 -22 -22 -46 Z"/>
        <circle cx="0" cy="14" r="19" fill="none" stroke="currentColor" stroke-width="9"/>
        <path d="M-8 14 c0 -8 5 -8 5 0 c0 -8 5 -8 5 0 c0 -8 5 -8 5 0" fill="none" stroke="currentColor" stroke-width="3"/>
        <rect x="18" y="26" width="18" height="5"/>
        <rect x="36" y="23" width="5" height="11"/>
      </g>
    </symbol>

    <symbol id="rattle" viewBox="-50 -50 100 100">
      <g fill="currentColor">
        <circle cx="10" cy="-12" r="22"/>
        <circle cx="10" cy="-36" r="8"/><circle cx="34" cy="-12" r="8"/>
        <circle cx="10" cy="12" r="8"/><circle cx="-14" cy="-12" r="8"/>
        <circle cx="27" cy="-29" r="8"/><circle cx="27" cy="5" r="8"/>
        <circle cx="-7" cy="-29" r="8"/><circle cx="-7" cy="5" r="8"/>
        <circle cx="10" cy="-12" r="10" fill="var(--halo)"/>
        <path d="M-4 6 L-24 28" stroke="currentColor" stroke-width="8" stroke-linecap="round"/>
        <circle cx="-30" cy="35" r="8" fill="none" stroke="currentColor" stroke-width="5"/>
      </g>
    </symbol>

    <symbol id="rings" viewBox="-50 -50 100 100">
      <g fill="none" stroke="currentColor" stroke-width="6">
        <circle cx="-13" cy="10" r="18"/>
        <circle cx="13" cy="10" r="18"/>
      </g>
      <polygon points="24,-30 34,-30 38,-24 29,-14 20,-24" fill="currentColor"/>
    </symbol>

    <symbol id="pins" viewBox="-50 -50 100 100">
      <g fill="currentColor">
        <path d="M16 -4 C4 -16 2 -40 16 -42 C30 -40 28 -16 16 -4 Z"/>
        <circle cx="16" cy="-28" r="5" fill="var(--halo)"/>
        <path d="M-20 26 C-32 14 -34 -10 -20 -12 C-6 -10 -8 14 -20 26 Z"/>
        <circle cx="-20" cy="2" r="5" fill="var(--halo)"/>
        <path d="M-10 22 C6 24 14 18 4 10 C-4 4 10 0 16 0" fill="none" stroke="currentColor" stroke-width="3" stroke-dasharray="5 4"/>
      </g>
    </symbol>

    <symbol id="house" viewBox="-50 -50 100 100">
      <g fill="currentColor">
        <polygon points="0,-34 -38,-2 -30,-2 0,-26 30,-2 38,-2"/>
        <rect x="18" y="-30" width="8" height="16"/>
        <rect x="-28" y="-6" width="56" height="38"/>
        <rect x="-7" y="8" width="14" height="24" fill="var(--halo)"/>
        <rect x="-22" y="2" width="10" height="10" fill="var(--halo)"/>
        <rect x="-42" y="30" width="84" height="5"/>
      </g>
    </symbol>

    <symbol id="cap" viewBox="-50 -50 100 100">
      <g fill="currentColor">
        <polygon points="0,-24 46,-8 0,8 -46,-8"/>
        <path d="M-28 0 V16 C-14 26 14 26 28 16 V0 L0 10 Z"/>
        <path d="M34 -6 V18" stroke="currentColor" stroke-width="3"/>
        <rect x="31" y="16" width="6" height="8"/>
      </g>
    </symbol>

    <symbol id="suitcase" viewBox="-50 -50 100 100">
      <g fill="currentColor">
        <rect x="-11" y="-44" width="22" height="12" rx="3" fill="none" stroke="currentColor" stroke-width="5"/>
        <rect x="-24" y="-34" width="48" height="66" rx="8"/>
        <rect x="-13" y="-24" width="5" height="46" rx="2" fill="var(--halo)"/>
        <rect x="-2.5" y="-24" width="5" height="46" rx="2" fill="var(--halo)"/>
        <rect x="8" y="-24" width="5" height="46" rx="2" fill="var(--halo)"/>
        <rect x="-18" y="32" width="8" height="8" rx="2"/>
        <rect x="10" y="32" width="8" height="8" rx="2"/>
      </g>
    </symbol>

    <symbol id="bunting" viewBox="-50 -50 100 100">
      <g fill="currentColor">
        <path d="M-44 -34 Q0 -18 44 -38" fill="none" stroke="currentColor" stroke-width="3"/>
        <polygon points="-40,-32 -26,-27 -34,-14"/>
        <polygon points="-20,-25 -4,-23 -12,-10"/>
        <polygon points="2,-23 18,-26 11,-11"/>
        <polygon points="24,-28 40,-34 35,-19"/>
        <path d="M-44 4 Q0 18 44 0" fill="none" stroke="currentColor" stroke-width="3"/>
        <polygon points="-40,6 -24,10 -31,24"/>
        <polygon points="-18,11 -2,12 -10,26"/>
        <polygon points="4,12 20,9 13,24"/>
        <polygon points="26,7 40,2 35,17"/>
      </g>
    </symbol>

    <symbol id="peg" viewBox="-50 -50 100 100">
      <g fill="currentColor" transform="rotate(-40)">
        <rect x="-46" y="-10" width="92" height="8" rx="3"/>
        <rect x="-46" y="2" width="92" height="8" rx="3"/>
        <rect x="-6" y="-14" width="16" height="28" rx="3"/>
        <circle cx="2" cy="0" r="4" fill="var(--halo)"/>
      </g>
    </symbol>

    <symbol id="glasses" viewBox="-50 -50 100 100">
      <g fill="currentColor">
        <g transform="rotate(-20 -14 0)">
          <path d="M-24 -30 H-6 L-9 2 C-10 8 -18 8 -19 2 Z"/>
          <rect x="-16" y="6" width="4" height="26"/>
          <rect x="-24" y="30" width="20" height="4"/>
        </g>
        <g transform="rotate(20 14 0)">
          <path d="M6 -30 H24 L21 2 C20 8 12 8 11 2 Z"/>
          <rect x="14" y="6" width="4" height="26"/>
          <rect x="6" y="30" width="20" height="4"/>
        </g>
        <path d="M0 -46 V-38 M-12 -44 L-8 -38 M12 -44 L8 -38" stroke="currentColor" stroke-width="3"/>
      </g>
    </symbol>
  </defs>

  <!-- frame and paper -->
  <rect class="frame" x="355" y="106" width="1222" height="1720" fill="var(--frame)"/>
  <rect class="paper" x="382" y="133" width="1168" height="1666" fill="url(#paperGlow)"/>

  <!-- title -->
  <path class="title-band" role="img" aria-label="Goldener Pinselstrich hinter dem Titel" d="M612 150 L1320 138 L1330 180 L1310 240 L606 246 L618 196 Z" fill="url(#titleBand)"/>
  <text class="title" x="968" y="214" textLength="600" lengthAdjust="spacingAndGlyphs">Road to 50 Years</text>

  <!-- treble clef -->
  <g class="clef-group">
    <path class="clef" d="M452 585 C455 600 470 595 468 580 L446 380 C442 352 478 352 474 388 C470 425 402 450 400 500 C398 540 452 548 472 520 C488 498 468 468 442 474 C420 480 420 506 438 510"/>
    <circle class="clef-dot" cx="430" cy="580" r="13"/>
  </g>

  <!-- staff 1 -->
  <g class="staff">
    <g class="staff-line"><line x1="430" y1="407" x2="1533" y2="407"/><line x1="430" y1="438" x2="1533" y2="438"/><line x1="430" y1="469" x2="1533" y2="469"/><line x1="430" y1="500" x2="1533" y2="500"/><line x1="430" y1="530" x2="1533" y2="530"/></g>
    <g class="bar-line"><line x1="745" y1="405" x2="745" y2="532"/><line x1="1043" y1="405" x2="1043" y2="532"/><line x1="1533" y1="405" x2="1533" y2="532"/></g>
  </g>
  <!-- staff 2 -->
  <g class="staff">
    <g class="staff-line"><line x1="432" y1="720" x2="1533" y2="720"/><line x1="432" y1="751" x2="1533" y2="751"/><line x1="432" y1="782" x2="1533" y2="782"/><line x1="432" y1="813" x2="1533" y2="813"/><line x1="432" y1="844" x2="1533" y2="844"/></g>
    <g class="bar-line"><line x1="432" y1="718" x2="432" y2="846"/><line x1="745" y1="718" x2="745" y2="846"/><line x1="1043" y1="718" x2="1043" y2="846"/><line x1="1533" y1="718" x2="1533" y2="846"/></g>
  </g>
  <!-- staff 3 -->
  <g class="staff">
    <g class="staff-line"><line x1="432" y1="1034" x2="1533" y2="1034"/><line x1="432" y1="1065" x2="1533" y2="1065"/><line x1="432" y1="1096" x2="1533" y2="1096"/><line x1="432" y1="1127" x2="1533" y2="1127"/><line x1="432" y1="1158" x2="1533" y2="1158"/></g>
    <g class="bar-line"><line x1="432" y1="1032" x2="432" y2="1160"/><line x1="745" y1="1032" x2="745" y2="1160"/><line x1="1043" y1="1032" x2="1043" y2="1160"/><line x1="1382" y1="1032" x2="1382" y2="1160"/><line x1="1533" y1="1032" x2="1533" y2="1160"/></g>
  </g>
  <!-- staff 4 -->
  <g class="staff">
    <g class="staff-line"><line x1="432" y1="1347" x2="1533" y2="1347"/><line x1="432" y1="1378" x2="1533" y2="1378"/><line x1="432" y1="1409" x2="1533" y2="1409"/><line x1="432" y1="1440" x2="1533" y2="1440"/><line x1="432" y1="1471" x2="1533" y2="1471"/></g>
    <g class="bar-line"><line x1="432" y1="1345" x2="432" y2="1473"/><line x1="604" y1="1345" x2="604" y2="1473"/><line x1="1043" y1="1345" x2="1043" y2="1473"/><line x1="1382" y1="1345" x2="1382" y2="1473"/><line x1="1533" y1="1345" x2="1533" y2="1473"/></g>
  </g>
  <!-- staff 5 -->
  <g class="staff">
    <g class="staff-line"><line x1="432" y1="1660" x2="1530" y2="1660"/><line x1="432" y1="1691" x2="1530" y2="1691"/><line x1="432" y1="1722" x2="1530" y2="1722"/><line x1="432" y1="1753" x2="1530" y2="1753"/><line x1="432" y1="1784" x2="1530" y2="1784"/></g>
    <g class="bar-line"><line x1="432" y1="1658" x2="432" y2="1786"/><line x1="738" y1="1658" x2="738" y2="1786"/><line x1="1053" y1="1658" x2="1053" y2="1786"/><line x1="1512" y1="1658" x2="1512" y2="1786"/></g>
    <line class="final-bar" x1="1528" y1="1658" x2="1528" y2="1786"/>
  </g>

  <!-- event symbols -->
  <g class="icon">
    <use href="#violin" x="490" y="380" width="100" height="100"/>
    <use href="#horn" x="630" y="455" width="90" height="90"/>
    <use href="#horn" x="755" y="395" width="90" height="90"/>
    <use href="#rings" x="920" y="470" width="80" height="80"/>
    <use href="#pins" x="1085" y="405" width="80" height="80"/>
    <use href="#rattle" x="1245" y="460" width="80" height="80"/>
    <use href="#violin" x="1395" y="380" width="100" height="100"/>

    <use href="#pins" x="490" y="710" width="80" height="80"/>
    <use href="#violin" x="600" y="765" width="100" height="100"/>
    <use href="#horn" x="755" y="705" width="90" height="90"/>
    <use href="#rattle" x="920" y="770" width="80" height="80"/>
    <use href="#horn" x="1075" y="705" width="90" height="90"/>
    <use href="#house" x="1250" y="775" width="80" height="80"/>
    <use href="#horn" x="1405" y="705" width="90" height="90"/>

    <use href="#violin" x="485" y="1005" width="100" height="100"/>
    <use href="#horn" x="630" y="1080" width="90" height="90"/>
    <use href="#horn" x="755" y="1020" width="90" height="90"/>
    <use href="#violin" x="910" y="1070" width="100" height="100"/>
    <use href="#bunting" x="1085" y="1025" width="80" height="80"/>
    <use href="#cap" x="1240" y="1100" width="90" height="90"/>
    <use href="#cap" x="1405" y="1010" width="90" height="90"/>

    <use href="#cap" x="485" y="1320" width="90" height="90"/>
    <use href="#house" x="630" y="1405" width="80" height="80"/>
    <use href="#suitcase" x="760" y="1335" width="80" height="80"/>
    <use href="#cap" x="915" y="1405" width="90" height="90"/>
    <use href="#peg" x="1080" y="1330" width="90" height="90"/>
    <use href="#rings" x="1243" y="1415" width="80" height="80"/>
    <use href="#rattle" x="1410" y="1340" width="80" height="80"/>

    <use href="#suitcase" x="490" y="1650" width="80" height="80"/>
    <use href="#rattle" x="625" y="1710" width="80" height="80"/>
    <use href="#suitcase" x="760" y="1650" width="80" height="80"/>
    <use href="#rattle" x="920" y="1710" width="80" height="80"/>
    <use href="#rings" x="1085" y="1630" width="80" height="80"/>
    <use href="#suitcase" x="1243" y="1710" width="80" height="80"/>
    <use href="#glasses" x="1410" y="1635" width="90" height="90"/>
  </g>

  <!-- row 1 labels -->
  <g class="labels">
    <text class="year" x="532" y="298">1972:</text><text class="event" x="532" y="327">Lore Bühne Ulm</text>
    <text class="year" x="665" y="366">1973:</text><text class="event" x="665" y="395">Berti Ankunft Ulm</text>
    <text class="year" x="800" y="298">1974:</text><text class="event" x="800" y="327">Berti Neckar-</text><text class="event" x="800" y="356">Philharmonie</text>
    <text class="year" x="960" y="298">1975:</text><text class="event" x="960" y="327">Lore &amp; Berti</text><text class="event" x="960" y="356">Hochzeit Ulm,</text><text class="event" x="960" y="385">3. Januar</text>
    <text class="year" x="1123" y="298">1977:</text><text class="event" x="1123" y="327">Umzug nach</text><text class="event" x="1123" y="356">Stuttgart</text>
    <text class="year" x="1284" y="366">1978:</text><text class="event" x="1284" y="395">Geburt Annika</text>
    <text class="year" x="1451" y="298">1979:</text><text class="event" x="1451" y="327">Lore Musikschule</text><text class="event" x="1451" y="356">Am Hang</text>
  </g>
  <!-- row 2 labels -->
  <g class="labels">
    <text class="year" x="532" y="601">1980:</text><text class="event" x="532" y="630">Umzug Lindenweg 12</text>
    <text class="year" x="665" y="649">1980:</text><text class="event" x="665" y="678">Lore Landesoper</text><text class="event" x="665" y="707">Stuttgart</text>
    <text class="year" x="800" y="601">1982:</text><text class="event" x="800" y="630">Berti Tournee</text><text class="event" x="800" y="659">Südafrika</text>
    <text class="year" x="960" y="649">1982:</text><text class="event" x="960" y="678">Geburt Mareike</text>
    <text class="year" x="1123" y="601">1983:</text><text class="event" x="1123" y="630">Berti Rheinbühne</text><text class="event" x="1123" y="659">Mannheim</text>
    <text class="year" x="1284" y="649">1985:</text><text class="event" x="1284" y="678">Ferienhaus</text><text class="event" x="1284" y="707">Gyopárosfürdö</text>
    <text class="year" x="1451" y="601">1986:</text><text class="event" x="1451" y="630">Berti Festspiele</text><text class="event" x="1451" y="659">Frankenhöhe</text>
  </g>
  <!-- row 3 labels -->
  <g class="labels">
    <text class="year" x="532" y="914">1988:</text><text class="event" x="532" y="943">Lore Tournee</text><text class="event" x="532" y="972">Südamerika</text>
    <text class="year" x="665" y="963">1989:</text><text class="event" x="665" y="992">Berti Tournee</text><text class="event" x="665" y="1021">Japan</text>
    <text class="year" x="800" y="914">1990:</text><text class="event" x="800" y="943">Berti Tournee</text><text class="event" x="800" y="972">Japan</text>
    <text class="year" x="960" y="963">1990:</text><text class="event" x="960" y="992">Lore Tournee Moskau/</text><text class="event" x="960" y="1021">Leningrad</text>
    <text class="year" x="1123" y="914">1995:</text><text class="event" x="1123" y="943">Festival Aurelia</text>
    <text class="year" x="1284" y="963">1997:</text><text class="event" x="1284" y="992">Abitur Annika</text>
    <text class="year" x="1451" y="914">2002:</text><text class="event" x="1451" y="943">Studienabschluss</text><text class="event" x="1451" y="972">Annika</text>
  </g>
  <!-- row 4 labels -->
  <g class="labels">
    <text class="year" x="532" y="1227">2002:</text><text class="event" x="532" y="1256">Abitur Mareike</text>
    <text class="year" x="665" y="1276">2004:</text><text class="event" x="665" y="1305">Renoviertes Haus</text><text class="event" x="665" y="1334">Gyopárosfürdö</text>
    <text class="year" x="800" y="1227">2005:</text><text class="event" x="800" y="1256">Lore &amp; Berti Tournee</text><text class="event" x="800" y="1285">Japan/</text><text class="event" x="800" y="1314">Südkorea</text>
    <text class="year" x="960" y="1276">2006:</text><text class="event" x="960" y="1305">Studienabschluss</text><text class="event" x="960" y="1334">Mareike</text>
    <text class="year" x="1123" y="1227">2009:</text><text class="event" x="1123" y="1256">Lore &amp; Berti Marino</text>
    <text class="year" x="1284" y="1276">2010:</text><text class="event" x="1284" y="1305">Hochzeit Annika</text><text class="event" x="1284" y="1334">&amp; Marco</text>
    <text class="year" x="1451" y="1227">2012:</text><text class="event" x="1451" y="1256">Geburt Lena</text>
  </g>
  <!-- row 5 labels -->
  <g class="labels">
    <text class="year" x="532" y="1540">2015:</text><text class="event" x="532" y="1569">Urlaub New York/</text><text class="event" x="532" y="1598">Miami</text>
    <text class="year" x="665" y="1589">2015:</text><text class="event" x="665" y="1618">Geburt</text><text class="event" x="665" y="1647">Matteo</text>
    <text class="year" x="800" y="1540">2017:</text><text class="event" x="800" y="1569">Urlaub</text><text class="event" x="800" y="1598">Kalifornien</text>
    <text class="year" x="960" y="1589">2017:</text><text class="event" x="960" y="1618">Geburt Jonas</text>
    <text class="year" x="1123" y="1540">2021:</text><text class="event" x="1123" y="1569">Hochzeit</text><text class="event" x="1123" y="1598">Mareike &amp; Jens</text>
    <text class="year" x="1284" y="1589">2022:</text><text class="event" x="1284" y="1618">Urlaub Gran Canyon/</text><text class="event" x="1284" y="1647">Las Vegas</text>
    <text class="year" x="1451" y="1540">2025:</text><text class="event" x="1451" y="1569">Lore &amp; Berti 50.</text><text class="event" x="1451" y="1598">Hochzeitstag,</text><text class="event" x="1451" y="1627">3. Januar</text>
  </g>
</svg>
</div>
</body>
</html>
```